BRIARFELL Real Estate
Real Estate Developer
Project: BRIARFELL Real Estate
BRIARFELL Real Estate - Real Estate
Creative Brief
Use specific fonts
Up to the designer!
Professional
Matthias L. Halvik
Managing Director
BRIARFELL Real Estate GmbH & Co. KG Lindauer Gang 14 20417 Hamburg Germany
mlh@briarfellre.com
briarfellre.com
One-sided or two-sided cards are welcome and any of the three logos and its colour variations can be chosen!

```html
<!DOCTYPE html>
<html lang="en">
<head>
<meta charset="utf-8">
<title>BRIARFELL Real Estate – Business Card</title>
<link rel="stylesheet" href="https://fonts.googleapis.com/css2?family=Montserrat:wght@400;600;700&display=swap">
<style>
  :root {
    --backdrop: #d6d6d4;
    --card-white: #ffffff;
    --brand-green: #3a5634;
    --brand-green-dark: #2c4328;
    --ink: #3c3c3c;
    --ink-soft: #6d6d6d;
  }
  * { box-sizing: border-box; margin: 0; padding: 0; }
  html, body {
    width: 1200px; height: 895px; overflow: hidden;
    background: var(--backdrop);
    font-family: "Montserrat", Arial, sans-serif;
  }
  .stage {
    position: relative; width: 1200px; height: 895px;
    display: flex; align-items: center; justify-content: center; gap: 40px;
  }
  .card {
    position: relative; width: 540px; height: 309px;
    box-shadow: 0 6px 18px rgba(0,0,0,0.18);
    overflow: hidden;
  }
  /* Front */
  .card-front { background: var(--card-white); }
  .brand {
    position: absolute; top: 78px; left: 0; right: 0;
    display: flex; align-items: center; justify-content: center; gap: 12px;
  }
  .brand-dot {
    width: 44px; height: 44px; border-radius: 50%;
    background: var(--brand-green);
  }
  .brand-text { display: flex; flex-direction: column; }
  .brand-name {
    font-weight: 700; font-size: 30px; letter-spacing: 1px;
    color: var(--brand-green); line-height: 1;
  }
  .brand-tagline {
    font-weight: 600; font-size: 11px; letter-spacing: 6.5px;
    color: var(--ink-soft); margin-top: 4px;
  }
  .holder {
    position: absolute; top: 168px; left: 0; right: 0; text-align: center;
    font-size: 13px; font-weight: 600; color: var(--brand-green);
  }
  .holder .divider { margin: 0 6px; color: var(--ink-soft); font-weight: 400; }
  .contacts {
    position: absolute; left: 26px; right: 26px; bottom: 30px;
    font-size: 8.6px; color: var(--ink); line-height: 1;
  }
  .contact-row { display: flex; gap: 14px; margin-top: 8px; white-space: nowrap; }
  .contact-item { display: inline-flex; align-items: center; gap: 4px; }
  .contact-item svg { width: 10px; height: 10px; flex: none; }
  /* Back */
  .card-back { background: var(--brand-green); }
  .back-circle {
    position: absolute; left: 40px; top: 36px;
    width: 170px; height: 170px; border-radius: 50%;
    background: var(--card-white);
    display: flex; align-items: center; justify-content: center;
  }
  .back-circle .brand-name { font-size: 24px; }
  .back-url {
    position: absolute; right: 30px; bottom: 34px;
    font-size: 16px; letter-spacing: 2px; color: var(--card-white);
  }
</style>
</head>
<body>
<main class="stage">
  <section class="card card-front" aria-label="Business card front">
    <div class="brand">
      <div class="brand-dot"></div>
      <div class="brand-text">
        <span class="brand-name">BRIARFELL</span>
        <span class="brand-tagline">REAL ESTATE</span>
      </div>
    </div>
    <p class="holder">Matthias L. Halvik<span class="divider">|</span>Managing Director</p>
    <div class="contacts">
      <div class="contact-row">
        <span class="contact-item">
          <svg viewBox="0 0 10 10"><circle cx="5" cy="5" r="5" fill="var(--brand-green)"/><path d="M5 2.2a1.8 1.8 0 0 1 1.8 1.8C6.8 5.4 5 7.8 5 7.8S3.2 5.4 3.2 4A1.8 1.8 0 0 1 5 2.2z" fill="#fff"/></svg>
          BRIARFELL Real Estate GmbH &amp; Co. KG Lindauer Gang 14 20417 Hamburg Germany
        </span>
        <span class="contact-item">
          <svg viewBox="0 0 10 10"><circle cx="5" cy="5" r="5" fill="var(--brand-green)"/><path d="M3.2 2.5h1l.5 1.3-.6.5a3.5 3.5 0 0 0 1.6 1.6l.5-.6 1.3.5v1c0 .3-.3.6-.6.6A4.2 4.2 0 0 1 2.6 3.1c0-.3.3-.6.6-.6z" fill="#fff"/></svg>
          +49 (0)40 5550142
        </span>
      </div>
      <div class="contact-row">
        <span class="contact-item">
          <svg viewBox="0 0 10 10"><circle cx="5" cy="5" r="5" fill="var(--brand-green)"/><rect x="3.5" y="2.3" width="3" height="5.4" rx=".5" fill="#fff"/></svg>
          +49 (0)172 5550187
        </span>
        <span class="contact-item">
          <svg viewBox="0 0 10 10"><circle cx="5" cy="5" r="5" fill="var(--brand-green)"/><rect x="2.8" y="3.8" width="4.4" height="2.8" fill="#fff"/><rect x="3.6" y="2.5" width="2.8" height="1.6" fill="#fff"/></svg>
          +49 (0)40 5550143
        </span>
        <span class="contact-item">
          <svg viewBox="0 0 10 10"><circle cx="5" cy="5" r="5" fill="var(--brand-green)"/><rect x="2.6" y="3.2" width="4.8" height="3.6" fill="#fff"/><path d="M2.6 3.2 5 5.2l2.4-2" stroke="var(--brand-green)" stroke-width=".6" fill="none"/></svg>
          mlh@briarfellre.com
        </span>
        <span class="contact-item">
          <svg viewBox="0 0 10 10"><circle cx="5" cy="5" r="5" fill="var(--brand-green)"/><circle cx="5" cy="5" r="2.6" stroke="#fff" stroke-width=".7" fill="none"/><path d="M2.4 5h5.2M5 2.4v5.2" stroke="#fff" stroke-width=".6"/></svg>
          www.briarfellre.com
        </span>
      </div>
    </div>
  </section>

  <section class="card card-back" aria-label="Business card back">
    <div class="back-circle">
      <span class="brand-name">BRIARFELL</span>
    </div>
    <p class="back-url">www.briarfellre.com</p>
  </section>
</main>
</body>
</html>
```